Real Estate Newsletter

I would like a template created for a monthly newsletter; ideally, two pages long, including my photo, logo and contact info. I need it to look professional and be very easy for me to drop text into.

Target Market(s)

Past/current clients

Industry/Entity Type

Real Estate Agent

Font styles to use
Serif

Requirements
Must have
• My contact info/photo and logo
• (206) 555-0173
• mfintry@kelvora.com
• www.MarloFintry.com
Nice to have
• I need a template where I can easily drop contact. I need the template to look professional so I can print it and mail it to current and past clients.

```html
<!DOCTYPE html>
<html lang="en">
<head>
<meta charset="utf-8">
<title>Marlo Fintry – Real Estate Newsletter</title>
<link href="https://fonts.googleapis.com/css2?family=Libre+Baskerville:wght@400;700&display=swap" rel="stylesheet">
<style>
  :root{
    --backdrop:#d5d6da;
    --paper:#ffffff;
    --sidebar:#e3e2f2;
    --band:#d4b5d6;
    --navy:#2e3192;
    --ink:#111111;
    --photo-a:#c9b9a8;
    --photo-b:#6b4a36;
  }
  html,body{margin:0;padding:0;width:1200px;height:1200px;overflow:hidden;background:var(--backdrop);}
  body{position:relative;font-family:"Libre Baskerville",Georgia,serif;}
  .page{
    position:absolute;left:176px;top:0;width:864px;height:1221px;
    background:var(--paper);transform:scale(0.9828);transform-origin:top left;overflow:hidden;
  }
  .sidebar{position:absolute;left:21px;top:0;width:288px;height:100%;background:var(--sidebar);}
  .header-band{position:absolute;left:0;top:76px;width:100%;height:117px;background:var(--band);}
  .portrait{
    position:absolute;left:85px;top:48px;width:160px;height:160px;border-radius:50%;
    border:6px solid var(--band);box-sizing:border-box;
    background:radial-gradient(circle at 55% 45%,var(--photo-a),var(--photo-b) 70%,#f4f1f0 71%);
  }
  .brand{
    position:absolute;left:440px;top:133px;width:280px;text-align:center;
    font-size:22px;font-weight:700;color:var(--navy);display:flex;align-items:center;justify-content:center;gap:8px;
  }
  .brand .mark{width:14px;height:14px;border-radius:50%;background:var(--navy);}
  .side-block{position:absolute;left:41px;width:248px;text-align:center;color:var(--navy);}
  .side-title{
    border-top:2px dashed var(--navy);border-bottom:2px dashed var(--navy);
    height:57px;line-height:57px;font-size:18px;letter-spacing:2px;
  }
  .contact-item{font-size:14.5px;margin-top:12px;letter-spacing:.3px;}
  .contact-item svg{display:block;margin:0 auto 4px;}
  .date-line{font-size:14px;text-align:left;margin-top:18px;letter-spacing:.3px;}
  .date-line sup{font-size:8px;}
  .field{display:flex;font-size:14px;text-align:left;margin-top:17px;letter-spacing:.3px;}
  .field .label{width:114px;}
  .field .dots{flex:1;letter-spacing:1px;}
  .main{position:absolute;left:339px;width:489px;}
  .section-head{
    background:var(--band);height:44px;line-height:44px;text-align:center;
    color:var(--navy);font-size:20px;letter-spacing:.8px;
  }
  .body-text{font-size:13.2px;line-height:17.4px;color:var(--ink);text-align:justify;margin:0;letter-spacing:.25px;}
</style>
</head>
<body>
<div class="page">
  <div class="sidebar"></div>
  <div class="header-band"></div>
  <div class="portrait" role="img" aria-label="Portrait photo of the agent"></div>
  <div class="brand"><span class="mark"></span>MarloFintry</div>

  <section class="side-block" style="top:246px;">
    <div class="side-title">CONTACT</div>
    <div class="contact-item" style="margin-top:24px;">
      <svg width="18" height="18" viewBox="0 0 18 18"><circle cx="9" cy="9" r="9" fill="#000"/><path d="M6 4.5l1.6 2-1 1.2c.6 1.5 1.6 2.5 3 3.1l1.2-1 2 1.6-.9 1.6c-3.6-.3-6.3-3-6.6-6.6z" fill="#fff"/></svg>
      (206) 555-0173
    </div>
    <div class="contact-item" style="margin-top:22px;">
      <svg width="18" height="18" viewBox="0 0 18 18"><circle cx="9" cy="9" r="8" fill="none" stroke="#000" stroke-width="1.6"/><rect x="5" y="6" width="8" height="6" fill="none" stroke="#000" stroke-width="1.2"/><path d="M5 6l4 3.5L13 6" fill="none" stroke="#000" stroke-width="1.2"/></svg>
      mfintry@kelvora.com
    </div>
    <div class="contact-item" style="margin-top:20px;">
      <svg width="20" height="20" viewBox="0 0 20 20" fill="none" stroke="#000" stroke-width="1.4"><circle cx="10" cy="10" r="8.5"/><ellipse cx="10" cy="10" rx="3.8" ry="8.5"/><path d="M1.5 10h17M3 5.5h14M3 14.5h14"/></svg>
      www.MarloFintry.com
    </div>
  </section>

  <section class="side-block" style="top:571px;">
    <div class="side-title">DATE</div>
    <div class="date-line">[example] 12<sup>th</sup> February 2018</div>
  </section>

  <section class="side-block" style="top:762px;">
    <div class="side-title">TO :</div>
    <div class="field"><span class="label">Client Name :</span><span class="dots">.....................</span></div>
    <div class="field"><span class="label">Phone&nbsp;&nbsp;&nbsp;&nbsp;&nbsp;&nbsp;&nbsp;&nbsp;&nbsp;&nbsp;&nbsp;&nbsp;:</span><span class="dots">.....................</span></div>
    <div class="field"><span class="label">Email&nbsp;&nbsp;&nbsp;&nbsp;&nbsp;&nbsp;&nbsp;&nbsp;&nbsp;&nbsp;&nbsp;&nbsp;&nbsp;:</span><span class="dots">.....................</span></div>
    <div class="field"><span class="label">Address&nbsp;&nbsp;&nbsp;&nbsp;&nbsp;&nbsp;&nbsp;&nbsp;:</span><span class="dots">.....................</span></div>
  </section>

  <article class="main" style="top:245px;">
    <h2 class="section-head" style="margin:0 0 14px;font-weight:400;">The Real Estate Market</h2>
    <p class="body-text">Many buyers and sellers are left feeling overwhelmed with the process and where to even begin. My job is to explain and guide you through the entire real estate process, from the initial meeting through the closing. I will be available day in and out to answer any questions you may have and address any concerns. My goal is that you feel you have my undivided attention during this process. I've spent my entire life in Seattle- born and raised in the Greenlake area- and I currently reside in Shoreline, after recently relocating from Lake Forest Park. On the side, my husband and I rehab and manage our rental properties. This side hobby has given me a unique perspective on handling renovations, local rents, and the potential appreciation of properties.</p>
    <p class="body-text" style="margin-top:17px;">I love what I do and the people I get to work with. I would be honored to walk through this process with you.</p>
  </article>

  <article class="main" style="top:630px;">
    <h2 class="section-head" style="margin:0 0 4px;font-weight:400;">Information</h2>
    <p class="body-text">We're all familiar with the ValueGuess, available on Homevalo, but did you know that the algorithm used to generate your ValueGuess can't actually take into account your home's updates, condition, street conditions or curb appeal? The only way to truly find out what your home is worth is to have a quick market analysis done. With just a few answers below, I can send you a quick market analysis that will give you a general idea of what your home would sell for in today's market.</p>
  </article>
</div>
</body>
</html>
```